Website for Law Firm in California with Existing Logo (Squarespace)

Thank you for participating.

I need a website for a law firm based in Orange County, California, called "Hollis Legal Group." The firm will provide civil litigation and business advice services. The principal practice areas include business litigation, real estate litigation, construction litigation, and other general commercial litigation.

I practiced at a very large, international law firm for 10 years (Mertwick Dunlow LLP) before starting Hollis Legal Group.

At the moment, Hollis Legal Group has one attorney, Gareth M. Hollis (me).

I have a logo for Hollis Legal Group (see attached files, including vectors and transparent background)--which is dark blue and gray. I am open to color changes/tweaks, but would prefer designs that communicate dependability, competence, sophistication, and trustworthiness.

The site should include a home page, as well as separate pages containing: (1) information about the firm and Gareth Hollis (e.g., "About"); (2) information about the firm's practice areas (use "Practice Areas"); (3) a "Contact Us" page where the visitor can insert contact information and describe their legal problem or help sought; (4) a page for articles and blog posts.

I'd also like to mention the practice areas on the main page with links to pages dedicated to each practice area. My thought is that these "practice areas" pages will have a similar look and design, but I will, of course, alter the content for each one.

The practice areas to list for now (I may add more or remove some later are):

Business Litigation
Real Estate Litigation
Banking & Lending Litigation
Contract Disputes
Construction Litigation
Commercial Litigation
Fraud Claims
Breach of Fiduciary Claims
Creditor's Rights
Judgment Collection
Appellate Law
Consumer and Personal Injury Claims
ADA Disputes
Other Civil Litigation
General Corporate Advice
Contract Review
Business Entity Formation

Each page should include easily viewable contact information without appearing cheesy.

I uploaded some head shots and photos of my building as well. They need not all be used. Feel free to play with adjustments to the photos (B&W, contrast, etc.).

I own and reserve the copyright to all files, logos, and pictures uploaded with this design.

I will provide a description of the firm and Gareth Hollis for the about page, as well as a summary of each practice area for the practice area page.

I will also need the ability to put a small description of the localities served by the firm at the bottom of each page on the site, along with a website disclaimer about representations made (I will provide the language for this too).

I am contemplating creating additional websites for different practice areas as well. So this may grow into a larger project if your design is selected. I will likely want to link to those sites from my home site if it makes sense to do so.

Thank you.
Updates

Project Deadline Extended
Reason: I was involved in a car incident yesterday and need a few more days to review designs. Thanks.

Target Market(s)

Legal Services for businesses and business owners, also individuals.

Industry/Entity Type

Attorney

Contact Information for Business Card

Please include my name and the title "Managing Attorney." Please include fields for my address, telephone number, and email address. Also please include "Orange County" and "Los Angeles" on the card.

Font styles to use
Sans Serif

Requirements
Must have
• See description
Nice to have
• See description
Should not have
• See description

```html
<!DOCTYPE html>
<html lang="en">
<head>
<meta charset="utf-8">
<title>Hollis Legal Group — Website Pages</title>
<link rel="stylesheet" href="https://fonts.googleapis.com/css2?family=Cinzel:wght@400;600&family=Lato:wght@400;700&display=swap">
<style>
  :root{
    --navy:#102b78;
    --lime:#8cc63f;
    --white:#ffffff;
    --ink:#2b2b2b;
    --grey:#6b6b6b;
    --body:#4a4a4a;
    --serif:'Cinzel', Georgia, serif;
    --sans:'Lato', Arial, sans-serif;
  }
  *{box-sizing:border-box;margin:0;padding:0}
  html,body{width:1200px;height:848px;overflow:hidden;background:#fff}
  body{position:relative;font-family:var(--sans);color:var(--ink)}

  .page{position:absolute;background:#fff;overflow:hidden;box-shadow:0 0 4px rgba(0,0,0,.25)}
  .page--home{left:59px;top:36px;width:332px;height:770px}
  .page--about{left:430px;top:36px;width:332px;height:770px}
  .page--practice{left:808px;top:36px;width:322px;height:419px}
  .page--contact{left:808px;top:467px;width:322px;height:339px}

  /* header */
  .site-header{position:absolute;left:0;top:0;right:0;height:28px;background:var(--navy);display:flex;align-items:center;justify-content:space-between;padding:0 14px 0 16px}
  .brand{font-family:var(--serif);font-weight:600;color:var(--white);font-size:9.5px;letter-spacing:.5px;white-space:nowrap}
  .nav{display:flex;gap:12px;list-style:none}
  .nav li{font-family:var(--serif);color:var(--white);font-size:5.6px;letter-spacing:.3px}
  .contact-strip{position:absolute;left:0;right:0;top:28px;height:10px;background:var(--lime);color:var(--white);font-size:4.6px;text-align:right;padding-right:14px;line-height:10px;letter-spacing:.2px;z-index:2}
  .contact-strip em{font-style:italic;font-family:Georgia,serif;font-size:5.4px}
  .contact-strip b{font-weight:700}

  /* imagery areas */
  .photo{position:absolute}
  .photo--tower{left:0;top:38px;width:100%;height:224px;
    background:radial-gradient(circle at 22% 10%,#ffffff 0%,rgba(255,255,255,.85) 8%,rgba(255,255,255,0) 30%),
               linear-gradient(160deg,#cfe2fa 0%,#7fa9e4 25%,#3f74c2 55%,#1e4a95 80%,#15305e 100%)}
  .photo--about-tower{left:0;top:38px;width:100%;height:224px;
    background:linear-gradient(180deg,#cfe0f4 0%,#7aa3d8 40%,#8fb3e0 58%,#dfe9f6 74%,#ffffff 84%)}
  .photo--portrait{left:150px;top:44px;width:172px;height:224px;
    background:radial-gradient(ellipse 48% 56% at 50% 58%,#f6f8fb 0%,#e6edf6 55%,rgba(230,237,246,0) 100%)}
  .photo--contract{left:0;top:38px;width:100%;height:190px;
    background:linear-gradient(180deg,#cfc9bf 0%,#e2ded8 40%,#f3f1ee 72%,#ffffff 100%)}
  .photo--entrance{left:0;top:38px;width:100%;height:135px;
    background:linear-gradient(180deg,#9fbd98 0%,#bfd0c3 35%,#cfd8de 70%,#f6f6f6 100%)}
  .photo--frame{border:2px solid var(--navy)}
  .photo--building-a{background:linear-gradient(165deg,#d4e0ea 0%,#9bb2c6 40%,#7d9a84 75%,#5d7d5e 100%)}
  .photo--building-b{background:linear-gradient(170deg,#d6e6f7 0%,#7aa2d6 45%,#46699f 85%,#4e6c48 100%)}
  .photo--map{background:linear-gradient(135deg,#eceee8,#dde1d9 55%,#cdd6e2)}

  /* home hero text */
  .hero-copy{position:absolute;left:0;right:0;top:118px;text-align:center;color:var(--white)}
  .hero-brand{font-family:var(--serif);font-weight:600;font-size:18px;letter-spacing:1px;margin-bottom:10px}
  .hero-tagline{font-family:var(--serif);font-size:6.8px;line-height:8px;letter-spacing:.4px}
  .hero-locale{font-family:var(--serif);font-size:5px;letter-spacing:.6px;margin-top:2px}

  /* practice areas grid */
  .section-title{position:absolute;left:0;right:0;top:272px;text-align:center;font-family:var(--serif);font-weight:600;color:var(--navy);font-size:11px;letter-spacing:.3px}
  .section-sub{position:absolute;left:0;right:0;top:287px;text-align:center;font-size:5px;color:var(--grey)}
  .tile{position:absolute;width:70px;height:62px;border:1.5px solid #c9cfdf;outline:1px solid var(--navy);background:var(--navy);box-shadow:0 1px 3px rgba(0,0,0,.4);overflow:hidden}
  .tile-img{height:36px}
  .tile-label{text-align:center;color:var(--white);font-family:var(--serif);font-weight:600;font-size:5.2px;line-height:5.6px;padding-top:3px}
  .tile-more{display:block;font-family:var(--sans);font-weight:400;font-size:3px;letter-spacing:.3px;margin-top:1px}

  /* page banners */
  .banner{position:absolute;left:0;height:28px;background:var(--navy);color:var(--white);font-family:var(--serif);font-weight:400;display:flex;align-items:center;z-index:2}
  .banner--about{top:151px;width:182px;padding-left:38px;font-size:13px;letter-spacing:.5px}
  .banner--practice{top:139px;width:182px;padding-left:44px;font-size:9.5px;letter-spacing:.4px;border:1px solid #fff;border-left:0}
  .banner--contact{top:100px;left:92px;width:148px;justify-content:center;font-size:10px;letter-spacing:.5px;border:1.5px solid #fff}

  /* body copy */
  .heading{position:absolute;font-family:var(--serif);font-weight:400;color:var(--ink);font-size:7.5px;letter-spacing:.3px;z-index:2}
  .meta{position:absolute;font-size:4.4px;color:var(--grey);z-index:2}
  .copy{position:absolute;font-size:4.1px;line-height:5.6px;color:var(--body);overflow:hidden;z-index:2}
  .bullets{position:absolute;left:44px;top:197px;list-style:none;font-size:4.6px;color:var(--body);line-height:10.5px}
  .bullets li::before{content:"•";margin-right:8px}

  /* contact form */
  .field{position:absolute;border:1px solid #aaa;background:#fff;font-size:4px;color:#666;padding:2px 3px}

  /* footer */
  .site-footer{position:absolute;left:0;right:0;background:var(--navy);color:var(--white);display:flex;align-items:center;justify-content:center;gap:8px}
  .footer-links{font-family:var(--serif);font-size:5.2px;letter-spacing:.3px}
</style>
</head>
<body>

<!-- Home -->
<section class="page page--home">
  <header class="site-header">
    <span class="brand">Hollis Legal Group</span>
    <ul class="nav"><li>Home</li><li>About</li><li>Practice Areas</li><li>Contact Us</li></ul>
  </header>
  <div class="contact-strip">ADDRESS DETAILS | <em>Call us today</em> <b>000-000-000</b></div>
  <div class="photo photo--tower" role="img" aria-label="Glass office tower against a bright sunlit sky with palm trees"></div>
  <div class="hero-copy">
    <div class="hero-brand">Hollis Legal Group</div>
    <div class="hero-tagline">Providing Civil Litigation<br>and Business Advice Services</div>
    <div class="hero-locale">Orange County | California</div>
  </div>

  <h2 class="section-title">PRACTICE AREAS</h2>
  <p class="section-sub">Sub heading here introducing practice areas</p>

  <div class="tile" style="left:54px;top:299px"><div class="tile-img" role="img" aria-label="Calculator and business papers" style="background:linear-gradient(155deg,#f2f4f6 0%,#c3cad3 40%,#3a3f47 75%,#8c96a4 100%)"></div><div class="tile-label">Business<br>Litigation<span class="tile-more">READ MORE</span></div></div>
  <div class="tile" style="left:131px;top:299px"><div class="tile-img" role="img" aria-label="Suburban house" style="background:linear-gradient(180deg,#a9c7e6 0%,#c7b594 45%,#8a6d4a 70%,#5f7a45 100%)"></div><div class="tile-label">Real Estate<br>Litigation<span class="tile-more">READ MORE</span></div></div>
  <div class="tile" style="left:207px;top:299px"><div class="tile-img" role="img" aria-label="Stack of banknotes" style="background:linear-gradient(160deg,#e3e7d4 0%,#a9b393 50%,#6f7a5c 100%)"></div><div class="tile-label">Banking &amp;<br>Lending Litigation<span class="tile-more">READ MORE</span></div></div>

  <div class="tile" style="left:54px;top:367px"><div class="tile-img" role="img" aria-label="Hand signing a contract" style="background:linear-gradient(160deg,#f1efeb 0%,#d9d3ca 55%,#a79f94 100%)"></div><div class="tile-label">Contract<br>Disputes<span class="tile-more">READ MORE</span></div></div>
  <div class="tile" style="left:131px;top:367px"><div class="tile-img" role="img" aria-label="Construction site with steel frame" style="background:linear-gradient(180deg,#8fb0d8 0%,#c98a55 45%,#a3582c 75%,#5c3d27 100%)"></div><div class="tile-label">Construction<br>Litigation<span class="tile-more">READ MORE</span></div></div>
  <div class="tile" style="left:207px;top:367px"><div class="tile-img" role="img" aria-label="Commercial office building" style="background:linear-gradient(170deg,#dce9f7 0%,#86a9da 40%,#3b64a8 100%)"></div><div class="tile-label">Commercial<br>Litigation<span class="tile-more">READ MORE</span></div></div>

  <div class="tile" style="left:54px;top:435px"><div class="tile-img" role="img" aria-label="Judge's gavel on a desk" style="background:linear-gradient(160deg,#1f1a17 0%,#6b4a30 45%,#a87a50 65%,#2a2420 100%)"></div><div class="tile-label">Fraud Claims<span class="tile-more">READ MORE</span></div></div>
  <div class="tile" style="left:131px;top:435px"><div class="tile-img" role="img" aria-label="Hands over documents at a meeting" style="background:linear-gradient(160deg,#6e5440 0%,#d1ae8b 50%,#8c6b50 100%)"></div><div class="tile-label">Breach of<br>Fiduciary Claims<span class="tile-more">READ MORE</span></div></div>
  <div class="tile" style="left:207px;top:435px"><div class="tile-img" role="img" aria-label="Business handshake" style="background:linear-gradient(160deg,#3c312a 0%,#9b7a60 50%,#d8c2ad 75%,#4a3d34 100%)"></div><div class="tile-label">Creditor's<br>Rights<span class="tile-more">READ MORE</span></div></div>

  <div class="tile" style="left:54px;top:503px"><div class="tile-img" role="img" aria-label="Professional at a desk with orange backdrop" style="background:linear-gradient(160deg,#e0701a 0%,#f2b471 45%,#eef1f5 70%,#c9d3df 100%)"></div><div class="tile-label">Judgment<br>Collection<span class="tile-more">READ MORE</span></div></div>
  <div class="tile" style="left:131px;top:503px"><div class="tile-img" role="img" aria-label="Gavel on sound block" style="background:linear-gradient(160deg,#191614 0%,#5e4330 45%,#b07f52 65%,#1f1b19 100%)"></div><div class="tile-label">Appellate Law<span class="tile-more">READ MORE</span></div></div>
  <div class="tile" style="left:207px;top:503px"><div class="tile-img" role="img" aria-label="Personal injury claim form" style="background:linear-gradient(160deg,#f0ebe4 0%,#d9c9b8 40%,#c0533a 70%,#8c3a2a 100%)"></div><div class="tile-label">Consumer &amp; Personal<br>Injury Claims<span class="tile-more">READ MORE</span></div></div>

  <div class="tile" style="left:54px;top:571px"><div class="tile-img" role="img" aria-label="Office worker at a bright workspace" style="background:linear-gradient(160deg,#eef2f6 0%,#c0cfdd 50%,#7f95ad 100%)"></div><div class="tile-label">ADA<br>Disputes<span class="tile-more">READ MORE</span></div></div>
  <div class="tile" style="left:131px;top:571px"><div class="tile-img" role="img" aria-label="Hands reviewing legal papers" style="background:linear-gradient(160deg,#4f4035 0%,#b39275 45%,#e2cfba 70%,#6e5a4a 100%)"></div><div class="tile-label">Other Civil<br>Litigation<span class="tile-more">READ MORE</span></div></div>
  <div class="tile" style="left:207px;top:571px"><div class="tile-img" role="img" aria-label="Advisor at desk with warm orange light" style="background:linear-gradient(160deg,#d9741c 0%,#f3b56c 45%,#f4ede3 75%,#d8d2c8 100%)"></div><div class="tile-label">General<br>Corporate Advice<span class="tile-more">READ MORE</span></div></div>

  <div class="tile" style="left:92px;top:639px"><div class="tile-img" role="img" aria-label="Pen resting on a printed contract" style="background:linear-gradient(160deg,#f3f1ee 0%,#d6d0c7 55%,#9f978b 100%)"></div><div class="tile-label">Contract<br>Review<span class="tile-more">READ MORE</span></div></div>
  <div class="tile" style="left:168px;top:639px"><div class="tile-img" role="img" aria-label="Laptop and documents on a dark desk" style="background:linear-gradient(160deg,#15171b 0%,#4d5561 45%,#9aa3ae 65%,#23262c 100%)"></div><div class="tile-label">Business Entity<br>Formation<span class="tile-more">READ MORE</span></div></div>

  <footer class="site-footer" style="top:716px;height:54px">
    <span class="brand">Hollis Legal Group</span>
    <span class="footer-links">Footer details | Social media links | disclaimer</span>
  </footer>
</section>

<!-- About -->
<section class="page page--about">
  <header class="site-header">
    <span class="brand">Hollis Legal Group</span>
    <ul class="nav"><li>Home</li><li>About</li><li>Practice Areas</li><li>Contact Us</li></ul>
  </header>
  <div class="contact-strip">ADDRESS DETAILS | <em>Call us today</em> <b>000-000-000</b></div>
  <div class="photo photo--about-tower" role="img" aria-label="Glass office tower and palm fronds under a blue sky"></div>
  <div class="photo photo--portrait" role="img" aria-label="Portrait of the managing attorney in a white shirt and striped tie"></div>
  <h1 class="banner banner--about">ABOUT US</h1>

  <h2 class="heading" style="left:38px;top:198px">GARETH M. HOLLIS</h2>
  <p class="meta" style="left:38px;top:208px">Details here etc</p>
  <div class="copy" style="left:38px;top:214px;width:132px;height:50px">
    We guide owners, lenders and families through disputes with steady, practical counsel. Every matter receives close attention, honest assessment and a clear plan from first call to final resolution. The practice serves companies and individuals across Orange County and Los Angeles with the care of a small firm and the depth of large firm training. Clients receive direct access to their attorney, timely updates on each filing and candid guidance on cost, risk and strategy before any decision is made.
  </div>

  <h2 class="heading" style="left:38px;top:288px">SUB HEADING</h2>
  <p class="meta" style="left:38px;top:298px">Details here etc</p>
  <div class="copy" style="left:38px;top:304px;width:117px;height:117px">
    The practice serves companies and individuals across Orange County and Los Angeles with the care of a small firm and the depth of large firm training. Clients receive direct access to their attorney, timely updates on each filing and candid guidance on cost, risk and strategy before any decision is made. From early negotiation through trial and appeal, the firm works to protect your business, your property and your peace of mind. We guide owners, lenders and families through disputes with steady, practical counsel. Every matter receives close attention, honest assessment and a clear plan from first call to final resolution. Clients receive direct access to their attorney, timely updates on each filing and candid guidance on cost, risk and strategy before any decision is made. From early negotiation through trial and appeal, the firm works to protect your business, your property and your peace of mind. The practice serves companies and individuals across Orange County and Los Angeles with the care of a small firm and the depth of large firm training.
  </div>
  <div class="photo photo--frame photo--building-a" style="left:161px;top:305px;width:133px;height:101px" role="img" aria-label="Office building entrance with palm trees"></div>

  <div class="copy" style="left:38px;top:422px;width:256px;height:67px">
    From early negotiation through trial and appeal, the firm works to protect your business, your property and your peace of mind. Clients receive direct access to their attorney, timely updates on each filing and candid guidance on cost, risk and strategy before any decision is made. We guide owners, lenders and families through disputes with steady, practical counsel. Every matter receives close attention, honest assessment and a clear plan from first call to final resolution. The practice serves companies and individuals across Orange County and Los Angeles with the care of a small firm and the depth of large firm training. Clients receive direct access to their attorney, timely updates on each filing and candid guidance on cost, risk and strategy before any decision is made. From early negotiation through trial and appeal, the firm works to protect your business, your property and your peace of mind. We guide owners, lenders and families through disputes with steady, practical counsel. Every matter receives close attention, honest assessment and a clear plan from first call to final resolution. The practice serves companies and individuals across Orange County and Los Angeles with the care of a small firm and the depth of large firm training.
  </div>

  <div class="copy" style="left:38px;top:492px;width:117px;height:106px">
    The practice serves companies and individuals across Orange County and Los Angeles with the care of a small firm and the depth of large firm training. Clients receive direct access to their attorney, timely updates on each filing and candid guidance on cost, risk and strategy before any decision is made. From early negotiation through trial and appeal, the firm works to protect your business, your property and your peace of mind. We guide owners, lenders and families through disputes with steady, practical counsel. Every matter receives close attention, honest assessment and a clear plan from first call to final resolution. Clients receive direct access to their attorney, timely updates on each filing and candid guidance on cost, risk and strategy before any decision is made. From early negotiation through trial and appeal, the firm works to protect your business, your property and your peace of mind. The practice serves companies and individuals across Orange County and Los Angeles with the care of a small firm and the depth of large firm training.
  </div>
  <div class="photo photo--frame photo--building-b" style="left:161px;top:492px;width:133px;height:101px" role="img" aria-label="Glass tower framed by palm trees"></div>

  <div class="copy" style="left:38px;top:600px;width:256px;height:84px">
    From early negotiation through trial and appeal, the firm works to protect your business, your property and your peace of mind. Clients receive direct access to their attorney, timely updates on each filing and candid guidance on cost, risk and strategy before any decision is made. We guide owners, lenders and families through disputes with steady, practical counsel. Every matter receives close attention, honest assessment and a clear plan from first call to final resolution. The practice serves companies and individuals across Orange County and Los Angeles with the care of a small firm and the depth of large firm training. Clients receive direct access to their attorney, timely updates on each filing and candid guidance on cost, risk and strategy before any decision is made. From early negotiation through trial and appeal, the firm works to protect your business, your property and your peace of mind. We guide owners, lenders and families through disputes with steady, practical counsel. Every matter receives close attention, honest assessment and a clear plan from first call to final resolution. The practice serves companies and individuals across Orange County and Los Angeles with the care of a small firm and the depth of large firm training. Clients receive direct access to their attorney, timely updates on each filing and candid guidance on cost, risk and strategy before any decision is made. From early negotiation through trial and appeal, the firm works to protect your business, your property and your peace of mind.
  </div>

  <footer class="site-footer" style="top:716px;height:54px">
    <span class="brand">Hollis Legal Group</span>
    <span class="footer-links">Footer details | Social media links | disclaimer</span>
  </footer>
</section>

<!-- Practice area: Contract Disputes -->
<section class="page page--practice">
  <header class="site-header">
    <span class="brand">Hollis Legal Group</span>
    <ul class="nav"><li>Home</li><li>About</li><li>Practice Areas</li><li>Contact Us</li></ul>
  </header>
  <div class="contact-strip">ADDRESS DETAILS | <em>Call us today</em> <b>000-000-000</b></div>
  <div class="photo photo--contract" role="img" aria-label="Hand with pen signing a printed contract"></div>
  <h1 class="banner banner--practice">CONTRACT DISPUTES</h1>

  <h2 class="heading" style="left:44px;top:184px;color:var(--navy)">SUB HEADING</h2>
  <ul class="bullets">
    <li>dot point details here summary</li>
    <li>dot point details here summary</li>
    <li>dot point details here summary</li>
    <li>dot point details here summary</li>
  </ul>
  <p class="meta" style="left:44px;top:250px">Details description here etc</p>
  <div class="copy" style="left:44px;top:256px;width:256px;height:34px">
    We guide owners, lenders and families through disputes with steady, practical counsel. Every matter receives close attention, honest assessment and a clear plan from first call to final resolution. Clients receive direct access to their attorney, timely updates on each filing and candid guidance on cost, risk and strategy before any decision is made. From early negotiation through trial and appeal, the firm works to protect your business, your property and your peace of mind. The practice serves companies and individuals across Orange County and Los Angeles with the care of a small firm and the depth of large firm training. We guide owners, lenders and families through disputes with steady, practical counsel.
  </div>

  <footer class="site-footer" style="top:367px;height:52px">
    <span class="brand">Hollis Legal Group</span>
    <span class="footer-links">Footer details | Social media links | disclaimer</span>
  </footer>
</section>

<!-- Contact -->
<section class="page page--contact">
  <header class="site-header">
    <span class="brand">Hollis Legal Group</span>
    <ul class="nav"><li>Home</li><li>About</li><li>Practice Areas</li><li>Contact Us</li></ul>
  </header>
  <div class="contact-strip">ADDRESS DETAILS | <em>Call us today</em> <b>000-000-000</b></div>
  <div class="photo photo--entrance" role="img" aria-label="Office building entrance lined with palm trees"></div>
  <h1 class="banner banner--contact">CONTACT US</h1>

  <div class="field" style="left:56px;top:186px;width:126px;height:11px">Name:</div>
  <div class="field" style="left:56px;top:202px;width:126px;height:11px">Phone:</div>
  <div class="field" style="left:56px;top:218px;width:126px;height:45px">Message:</div>
  <div class="photo photo--map" style="left:188px;top:186px;width:78px;height:77px" role="img" aria-label="Street map showing the office location"></div>

  <footer class="site-footer" style="top:287px;height:52px">
    <span class="brand">Hollis Legal Group</span>
    <span class="footer-links">Footer details | Social media links | disclaimer</span>
  </footer>
</section>

</body>
</html>
```